Ned Walcott Fairway Lessons Rack Card

The flyer will be a rack card. Front side only. Nothing on back. 3.75 inches by 8.5 inches. Or close to that. I’d like it to be as colorful as possible and to include several logos in different places.
The brochure is to attract golfers attention and still look traditional and classy not crazy or to artsy. Golf is a very traditional sport and would just like it to look professional and welcoming so golfers no I’m credible in my teaching and they will learn something. I will send a rough idea and a sample of one I had before but use your creative skills and ingenuity to design it. You will have to put my name: Ned Walcott under the TLQ logo. It is a requirement by the TLQ. Also the logo size must me .0875 inches high. If possible use a gotham or Hoefler text type or something businesslike or similar for my name. Also I am sorry for the different logos available on this file because I am not tech savvy so you will have to choose the best logo and cut it out of the grouping to match what you want to do. I am sorry for all the details. I will be available all weekend if you need more info. or help. I am sure you are very skilled and can tell I am not. Sorry. I laid out a sketch for you so you know what info. verbiage is important. and where to somewhat place the logos. Up to your skill for most of it. Your design! Go for it.!

Target Market(s)

Golfers of all ages from 18-70. Men and Women.

Industry/Entity Type

Golf Industry. Teaching and learning game if golf

Font styles to use
Sans Serif
Other font styles liked:
• Mixture maybe traditional type. Easy to read.

Colors

Designer to choose only greyscale colors for use in the design.

Requirements
Must have
• My JPG golf logo and the TLQ official logo. Also will send several other logos to put in. I will tell you where they should go on the rack card.
Nice to have
• Maybe a golf picture from a course with a green and flag as the one on my old brochure I’m sending or similar. It just adds color and eye catching
Should not have
• Nothing hard to read or difficult to comprehend. Pretty straight forward and quality and style in a traditional sense,

```html
<!DOCTYPE html>
<html lang="en">
<head>
<meta charset="utf-8">
<title>Ned Walcott Fairway Lessons Rack Card</title>
<link href="https://fonts.googleapis.com/css2?family=Figtree:wght@400;500;600;700;800&display=swap" rel="stylesheet">
<style>
  :root {
    --ink-dark: #1d1a1f;
    --ink-navy: #0f2a4a;
    --brand-blue: #1283c9;
    --brand-orange: #ffa200;
    --paper: #f4f4f4;
    --band-light: #e6e6e6;
    --white: #ffffff;
    --text-dark: #111111;
  }
  * { box-sizing: border-box; margin: 0; padding: 0; }
  html, body { width: 1200px; height: 2720px; overflow: hidden; }
  body {
    position: relative;
    background: var(--ink-dark);
    font-family: "Figtree", "Helvetica Neue", Arial, sans-serif;
    color: var(--white);
  }
  .backdrop { position: absolute; inset: 0; width: 1200px; height: 2720px; }

  .brand-name {
    position: absolute; left: 108px; top: 118px; width: 200px;
    color: var(--brand-blue); font-weight: 600; font-size: 30px; line-height: 1.05;
  }
  .contact { position: absolute; left: 107px; display: flex; align-items: center; gap: 22px; font-size: 21px; }
  .contact .icon { width: 47px; height: 47px; border-radius: 50%; background: var(--brand-blue); display: flex; align-items: center; justify-content: center; }
  .contact--web { top: 273px; }
  .contact--phone { top: 341px; }

  .hero-title { position: absolute; left: 107px; top: 440px; font-size: 39px; font-weight: 600; line-height: 1.16; }
  .hero-sub { position: absolute; left: 107px; top: 553px; font-size: 20px; font-weight: 500; }
  .hero-copy { position: absolute; left: 107px; width: 540px; font-size: 17px; line-height: 27.8px; }
  .hero-copy--one { top: 599px; }
  .hero-copy--two { top: 738px; }

  .card { position: absolute; left: 243px; top: 983px; width: 715px; height: 747px; background: var(--paper); color: var(--ink-navy); }
  .card-title { position: absolute; left: 107px; top: 45px; font-size: 38px; font-weight: 700; }

  .price { position: absolute; width: 213px; height: 215px; color: var(--white); }
  .price--blue { background: var(--brand-blue); }
  .price--orange { background: var(--brand-orange); }
  .price .reg { position: absolute; font-size: 15px; font-weight: 600; }
  .price .amount { position: absolute; font-size: 50px; font-weight: 700; line-height: 1; }
  .price .amount sup { font-size: 27px; vertical-align: top; position: relative; top: 2px; }
  .price .note { position: absolute; font-size: 20px; line-height: 26px; }

  .includes-title { position: absolute; left: 107px; top: 392px; font-size: 37px; font-weight: 700; }
  .includes-list { position: absolute; left: 127px; top: 445px; list-style: none; font-size: 21px; font-weight: 500; color: var(--text-dark); }
  .includes-list li { height: 41.6px; }
  .includes-list li::before { content: "\2022"; margin-right: 8px; }
  .level { position: absolute; left: 107px; top: 619px; font-size: 27px; font-weight: 600; color: var(--text-dark); }
  .more-info { position: absolute; left: 107px; top: 662px; font-size: 21px; font-weight: 500; color: var(--text-dark); }
  .more-info a { color: var(--brand-blue); text-decoration: none; }

  .partner-strip { position: absolute; left: 0; top: 1806px; width: 1200px; height: 112px; background: linear-gradient(90deg, #2a262b 0%, #8a878b 25%, #9d9b9d 55%, #d4d3d4 85%, #f4f4f4 100%); }
  .partner { position: absolute; top: 30px; font-size: 46px; font-weight: 800; line-height: 1; }
  .partner--one { left: 334px; color: var(--brand-orange); }
  .partner--two { left: 653px; color: #2b2526; }

  .package-title { position: absolute; left: 0; width: 1200px; top: 1995px; text-align: center; font-size: 39px; font-weight: 600; }
  .package-includes { position: absolute; left: 350px; top: 2350px; width: 620px; font-size: 23px; font-weight: 700; line-height: 38px; }
  .package-includes strong { font-size: 37px; font-weight: 600; }

  .seal { position: absolute; border-radius: 50%; width: 130px; height: 130px; }
  .seal--guarantee { left: 108px; top: 2563px; background: radial-gradient(circle, #c9a227 0 55%, #1d1a1f 56% 62%, #c9a227 63%); }
  .seal--member { left: 535px; top: 2561px; background: radial-gradient(circle, #2d4f7c 0 55%, #c8a96a 56% 66%, #2d4f7c 67%); }
  .membership { position: absolute; left: 851px; top: 2580px; width: 250px; font-size: 21px; font-weight: 700; line-height: 23px; color: var(--text-dark); }
</style>
</head>
<body>
  <svg class="backdrop" viewBox="0 0 1200 2720" aria-hidden="true">
    <defs>
      <linearGradient id="lightBand" x1="0" y1="0" x2="1" y2="0">
        <stop offset="0" stop-color="#f1f1f1"/>
        <stop offset="1" stop-color="#e2e2e2"/>
      </linearGradient>
    </defs>
    <polygon points="0,1216 1200,1088 1200,1547 0,1701" fill="url(#lightBand)"/>
    <polygon points="0,2549 1200,2496 1200,2720 0,2720" fill="var(--white)"/>
  </svg>

  <svg class="backdrop" viewBox="0 0 1200 2720" role="img" aria-label="Photo of a golf ball resting beside the cup on a sunlit putting green">
    <defs>
      <linearGradient id="greenPhoto" x1="1" y1="0" x2="0.4" y2="1">
        <stop offset="0" stop-color="#c8b31a"/>
        <stop offset="0.35" stop-color="#6f8a1e"/>
        <stop offset="0.75" stop-color="#2f4a12"/>
        <stop offset="1" stop-color="#1a2410"/>
      </linearGradient>
    </defs>
    <polygon points="1029,0 1200,0 1200,949 503,427" fill="url(#greenPhoto)"/>
  </svg>

  <div class="brand-name">Ned Walcott Fairway Lessons</div>

  <div class="contact contact--web">
    <span class="icon">
      <svg width="24" height="24" viewBox="0 0 24 24" fill="none" stroke="#fff" stroke-width="1.8"><circle cx="12" cy="12" r="9"/><ellipse cx="12" cy="12" rx="4" ry="9"/><line x1="3" y1="12" x2="21" y2="12"/></svg>
    </span>
    <span>nwalcottgolf.com</span>
  </div>
  <div class="contact contact--phone">
    <span class="icon">
      <svg width="22" height="22" viewBox="0 0 24 24" fill="#fff"><path d="M6.6 10.8a15.1 15.1 0 0 0 6.6 6.6l2.2-2.2a1 1 0 0 1 1-.25 11.4 11.4 0 0 0 3.6.57 1 1 0 0 1 1 1V20a1 1 0 0 1-1 1A17 17 0 0 1 3 4a1 1 0 0 1 1-1h3.5a1 1 0 0 1 1 1c0 1.25.2 2.45.57 3.57a1 1 0 0 1-.25 1z"/></svg>
    </span>
    <span>555-014-2376</span>
  </div>

  <h1 class="hero-title">Unleash Your<br>Potential on the Green</h1>
  <p class="hero-sub">Golf Lessons Tailored to Your Skill Level</p>
  <p class="hero-copy hero-copy--one">Whether you're a beginner looking to learn the fundamentals or an experienced golfer aiming to refine your technique, Ned Walcott Fairway Lessons offers personalized golf lessons suited to your skill level.</p>
  <p class="hero-copy hero-copy--two">Our experienced instructors will provide expert guidance, helping you improve your swing, accuracy, and overall performance on the course. Take your game to the next level with our comprehensive golf lessons designed to meet your specific needs.</p>

  <section class="card">
    <h2 class="card-title">Golf Swing Analysis</h2>
    <div class="price price--blue" style="left:107px; top:133px;">
      <span class="amount" style="left:38px; top:67px;">$59<sup>.99</sup></span>
      <span class="note" style="left:38px; top:125px;">1 hour analysis</span>
    </div>
    <div class="price price--blue" style="left:395px; top:133px;">
      <span class="reg" style="left:51px; top:43px;">Reg.</span>
      <span class="amount" style="left:51px; top:67px;">$79<sup>00</sup></span>
      <span class="note" style="left:38px; top:122px;">One time<br>limited offer</span>
    </div>
    <h3 class="includes-title">Includes:</h3>
    <ul class="includes-list">
      <li>Swing analysis W/Video</li>
      <li>Review swing technique</li>
      <li>Suggested tips &amp; tricks</li>
      <li>Video &amp; Summary sent to your mobile devices</li>
    </ul>
    <p class="level">From Beginners to Advanced</p>
    <p class="more-info">For more information visit <a href="#">Nwalcottlessons.com</a></p>
  </section>

  <div class="partner-strip">
    <span class="partner partner--one">Strikewise</span>
    <span class="partner partner--two">Trackline</span>
  </div>

  <h2 class="package-title">Special Lesson Package</h2>
  <div class="price price--orange" style="left:350px; top:2105px;">
    <span class="reg" style="left:47px; top:42px;">Reg.</span>
    <span class="amount" style="left:47px; top:66px;">$237</span>
    <span class="note" style="left:47px; top:122px; width:120px; text-align:center;">3- one hours lessons</span>
  </div>
  <div class="price price--orange" style="left:638px; top:2105px;">
    <span class="amount" style="left:49px; top:70px;">$225</span>
    <span class="note" style="left:38px; top:128px;">1 hour analysis</span>
  </div>
  <p class="package-includes"><strong>Includes:</strong> Video Analysis, Lessons Summery &amp; Video review sent to mobile device, Tips &amp; tricks, and action plans to improve.</p>

  <div class="seal seal--guarantee" role="img" aria-label="Satisfaction guarantee seal"></div>
  <div class="seal seal--member" role="img" aria-label="Professional association member seal"></div>
  <p class="membership">Ned Walcott Course a member QTR. Century member TLQ</p>
</body>
</html>
```